Flyer to advertise gutter cleaning throughout the Autumn and winter monthss

I need a new flyer to advertise gutter and driveway cleaning, roof and gutter repairs.

I am an experienced licensed Plumber and Gasfitter looking to broaden my scope of work to gutter cleaning. I am experienced in cleaning gutter and live in a area with large gum trees. I wont something that's clear, eye catching but not too busy.

Flyer requirements: Free roof inspection - no obligation. Gutter Cleaning from $199. Pictures of men using blower or hands to clean roof gutters (no obvious faces) to be included. Australian looking houses.

A mention that 'All general plumbing maintenance' is offered as other services but not too much wording about this as the target is for gutter cleaning.

Phone number: 0437 582 316 (in this format)
Business Name: Bracken Plumbing & Gasfitting
License: 3817502
ABN: 71395046287
Web: http://brackenplumbing.example-site.net/

Target Market(s)

Elderly - busy working class

Industry/Entity Type

Plumber

Font styles to use
Sans Serif

Colors
0355a3
fbed22
ec1f27
f78f20

Requirements
Must have
• Roof Gutter Cleaning pictures
• Men in protective clothing if possible
Nice to have
• More information:
• Prevent against flooding, mold, rust, rotting and corrosion now!
• Gutter Cleaning Services
• • Remove leaves, sticks, and other debris
• • Clear away clogs
• • Test your downpipes
• • Pinpoint any gutter issues
• • Repair gutter
• With regular service, you can count on your property to be well-protected no matter what the forecast!
Should not have
• Houses that don't look Australian

```html
<!DOCTYPE html>
<html lang="en">
<head>
<meta charset="utf-8">
<title>Bracken Plumbing &amp; Gasfitting – Gutter Cleaning Flyer</title>
<link href="https://fonts.googleapis.com/css2?family=Open+Sans:wght@400;600;700&family=Oswald:wght@600;700&display=swap" rel="stylesheet">
<style>
  :root {
    --blue: #0355a3;
    --blue-deep: #0b2f6b;
    --yellow: #fbed22;
    --yellow-deep: #e9c80f;
    --red: #ec1f27;
    --orange: #f78f20;
    --white: #ffffff;
    --ink: #1d1d1f;
    --mist: #e9eaec;
    --ring: #c9cbcf;
  }
  * { margin: 0; padding: 0; box-sizing: border-box; }
  html, body { width: 973px; height: 1200px; overflow: hidden; background: #f2f2f2; }
  .flyer {
    position: relative; width: 973px; height: 1200px; overflow: hidden;
    font-family: "Open Sans", Arial, sans-serif; color: var(--ink);
    background: var(--white);
  }
  .hero-photo {
    position: absolute; left: 0; top: 0; width: 973px; height: 447px;
    background: linear-gradient(180deg, #8fb8e6 0%, #dfe8f0 35%, #c9ccd0 60%, #6f9a4a 85%, #4f7d33 100%);
  }
  .brand {
    position: absolute; right: 60px; top: 72px;
    display: flex; align-items: center; gap: 12px;
  }
  .brand-dot { width: 44px; height: 44px; border-radius: 50%; background: var(--blue); }
  .brand-name {
    font-weight: 700; font-size: 22px; color: var(--blue-deep); line-height: 1.1; width: 250px;
  }
  .tagline-band {
    position: absolute; left: 0; top: 447px; width: 973px; height: 128px;
    background: linear-gradient(90deg, var(--blue) 0%, var(--blue-deep) 100%);
    display: flex; align-items: center; justify-content: center; text-align: center;
  }
  .tagline-band h1 {
    color: var(--white); font-weight: 700; font-size: 29px; line-height: 1.38; letter-spacing: 0.2px;
  }
  .services-area {
    position: absolute; left: 0; top: 575px; width: 973px; height: 543px;
    background: radial-gradient(ellipse at 50% 40%, #f7f7f8 0%, var(--mist) 70%, #dcdde0 100%);
  }
  .offer {
    position: absolute; border-radius: 50%;
    display: flex; flex-direction: column; align-items: center; justify-content: center; text-align: center;
  }
  .offer-ring { border: 2px solid var(--ring); background: rgba(255,255,255,0.4); }
  .offer-photo { color: var(--white); box-shadow: 0 6px 16px rgba(0,0,0,0.25); }
  .offer-photo.gutter { background: radial-gradient(circle at 40% 35%, #7d9a7a 0%, #4f5d54 60%, #3a3f3c 100%); }
  .offer-photo.driveway { background: radial-gradient(circle at 55% 40%, #7a7d82 0%, #4a4d52 60%, #2e3034 100%); }
  .offer-label { font-weight: 700; font-size: 22px; line-height: 1.3; }
  .offer-price { font-family: "Oswald", "Arial Narrow", sans-serif; font-weight: 700; font-size: 50px; line-height: 1.1; }
  .offer-free {
    background: radial-gradient(circle at 50% 40%, var(--yellow) 0%, var(--yellow-deep) 100%);
    color: var(--white); box-shadow: 0 10px 22px rgba(0,0,0,0.25); border: 4px solid rgba(255,255,255,0.6);
  }
  .offer-free .headline { font-family: "Oswald", "Arial Narrow", sans-serif; font-weight: 700; font-size: 36px; line-height: 1.15; }
  .offer-free .sub { font-weight: 700; font-size: 23px; margin-top: 4px; padding-bottom: 10px; border-bottom: 2px solid rgba(255,255,255,0.85); }
  .offer-free .credentials { font-size: 15px; line-height: 1.4; margin-top: 10px; }
  .service-list {
    position: absolute; left: 42px; top: 933px; width: 887px; height: 169px;
    border: 1.5px dotted var(--red); border-radius: 10px;
  }
  .service-title {
    position: absolute; left: 245px; top: -13px; width: 378px; height: 40px;
    background: var(--red); color: var(--white); border-radius: 8px;
    font-weight: 600; font-size: 20px; display: flex; align-items: center; justify-content: center;
  }
  .service-items {
    position: absolute; left: 20px; top: 50px; right: 20px;
    list-style: none; display: grid; grid-template-columns: 443px 1fr; row-gap: 10px;
  }
  .service-items li { display: flex; align-items: center; gap: 9px; font-size: 20px; font-weight: 400; height: 26px; }
  .bullet { width: 14px; height: 14px; flex: none; }
  .contact-bar { position: absolute; left: 0; top: 1118px; width: 973px; height: 82px; }
  .contact-band { position: absolute; left: 0; top: 0; }
  .contact-call {
    position: absolute; left: 70px; top: 0; height: 82px; display: flex; align-items: center;
    color: var(--white); font-size: 33px; font-weight: 400; letter-spacing: -0.2px; white-space: nowrap;
  }
  .contact-phone {
    position: absolute; left: 539px; top: 0; height: 82px; display: flex; align-items: center; gap: 22px;
    color: var(--white); font-weight: 700; font-size: 47px; letter-spacing: 3px; white-space: nowrap;
  }
  .phone-icon { flex: none; width: 46px; height: 46px; }
</style>
</head>
<body>
<main class="flyer">
  <div class="hero-photo" role="img" aria-label="Hand holding a pressure washer wand in front of a two-storey house with lawn and garden"></div>

  <div class="brand">
    <span class="brand-dot"></span>
    <span class="brand-name">Bracken Plumbing &amp; Gasfitting</span>
  </div>

  <section class="tagline-band">
    <h1>PREVENT AGAINST FLOODING, MOLD, RUST,<br>ROTTING AND CORROSION NOW!</h1>
  </section>

  <section class="services-area" role="img" aria-label="Water droplets on a light grey surface"></section>

  <div class="offer offer-ring" style="left:73px; top:620px; width:276px; height:272px;"></div>
  <div class="offer offer-photo gutter" role="img" aria-label="Gutter being cleared with a spray nozzle" style="left:86px; top:633px; width:250px; height:246px;">
    <span class="offer-label">GUTTER<br>CLEANING FROM</span>
    <span class="offer-price">$199</span>
  </div>

  <div class="offer offer-ring" style="left:602px; top:620px; width:276px; height:272px;"></div>
  <div class="offer offer-photo driveway" role="img" aria-label="Driveway being pressure cleaned" style="left:615px; top:633px; width:250px; height:246px;">
    <span class="offer-label">DRIVEWAY<br>CLEANING FROM</span>
    <span class="offer-price">$199</span>
  </div>

  <div class="offer offer-free" style="left:340px; top:613px; width:286px; height:286px;">
    <span class="headline">FREE ROOF<br>INSPECTION</span>
    <span class="sub">NO OBLIGATION</span>
    <span class="credentials">License: 3817502<br>ABN: 71395046287</span>
  </div>

  <section class="service-list">
    <h2 class="service-title">GUTTER CLEANING SERVICES</h2>
    <ul class="service-items">
      <li><svg class="bullet" viewBox="0 0 14 14"><circle cx="7" cy="7" r="7" fill="#ec1f27"/><path d="M5.5 4l3 3-3 3" stroke="#fff" stroke-width="1.8" fill="none"/></svg>Remove leaves, sticks, and other debris</li>
      <li><svg class="bullet" viewBox="0 0 14 14"><circle cx="7" cy="7" r="7" fill="#ec1f27"/><path d="M5.5 4l3 3-3 3" stroke="#fff" stroke-width="1.8" fill="none"/></svg>Pinpoint any gutter issues</li>
      <li><svg class="bullet" viewBox="0 0 14 14"><circle cx="7" cy="7" r="7" fill="#ec1f27"/><path d="M5.5 4l3 3-3 3" stroke="#fff" stroke-width="1.8" fill="none"/></svg>Clear away clogs</li>
      <li><svg class="bullet" viewBox="0 0 14 14"><circle cx="7" cy="7" r="7" fill="#ec1f27"/><path d="M5.5 4l3 3-3 3" stroke="#fff" stroke-width="1.8" fill="none"/></svg>Repair gutter</li>
      <li><svg class="bullet" viewBox="0 0 14 14"><circle cx="7" cy="7" r="7" fill="#ec1f27"/><path d="M5.5 4l3 3-3 3" stroke="#fff" stroke-width="1.8" fill="none"/></svg>Test your downpipes</li>
      <li><svg class="bullet" viewBox="0 0 14 14"><circle cx="7" cy="7" r="7" fill="#ec1f27"/><path d="M5.5 4l3 3-3 3" stroke="#fff" stroke-width="1.8" fill="none"/></svg>Your property will be well-protected</li>
    </ul>
  </section>

  <footer class="contact-bar">
    <svg class="contact-band" width="973" height="82" viewBox="0 0 973 82" aria-hidden="true">
      <defs>
        <linearGradient id="footBlue" x1="0" x2="1" y1="0" y2="0">
          <stop offset="0" stop-color="#0b2f6b"/><stop offset="1" stop-color="#0355a3"/>
        </linearGradient>
      </defs>
      <rect x="0" y="0" width="973" height="82" fill="url(#footBlue)"/>
      <polygon points="494,0 973,0 973,82 474,82" fill="#ffffff"/>
      <polygon points="503,0 973,0 973,82 483,82" fill="#f0c916"/>
    </svg>
    <span class="contact-call">CONTACT US TODAY!!!</span>
    <span class="contact-phone">
      <svg class="phone-icon" viewBox="0 0 46 46" aria-hidden="true">
        <circle cx="23" cy="23" r="20" fill="none" stroke="#fff" stroke-width="3"/>
        <path d="M16 13c1.5-1 3-.6 3.6.6l1.8 3.6c.5 1 .2 2-.6 2.6l-1.5 1.1c1 2.4 3 4.4 5.4 5.4l1.1-1.5c.6-.8 1.6-1.1 2.6-.6l3.6 1.8c1.2.6 1.6 2.1.6 3.6-1.5 2.2-4 3-6.6 1.8-4.5-2-8.2-5.7-10.2-10.2-1.2-2.6-.4-5.1 1.8-6.6z" fill="#fff"/>
      </svg>
      <span class="phone-number">0437 582 316</span>
    </span>
  </footer>
</main>
</body>
</html>
```